Calling All Web Design Visionaries: Transform the Meridian Vault Website!

Dear Web Design Innovators,

Are you ready to embark on a cosmic design journey? We are thrilled to announce an exciting opportunity to revamp and upgrade the Meridian Vault website, and we need your exceptional design prowess to bring our vision to life.

About Meridian Vault:
Meridian Vault is on a mission to reshape the future of space construction. We're pioneers in the field, developing cutting-edge concept construction blocks that promise to redefine how we build beyond our planet's boundaries. Our solutions are scalable, sustainable, and poised to accelerate humanity's journey into the cosmos.

Current Website:
Take a look at our current website [www.meridianvault-example.co.uk](https://www.meridianvault-example.co.uk) to get a glimpse of our existing online presence. While it served us well, we believe it's time for a transformative makeover.

Your Mission:
We're seeking imaginative web designers who can bring a fresh perspective to our online platform. Here's the website layout we're envisioning:
- Homepage: A futuristic and clean design that reflects our commitment to innovation. Clear navigation to key sections.
- About Us: A captivating section introducing our mission and team.
- Products: Highlighting our revolutionary concept construction blocks.
- Projects: Showcasing our involvement in space construction initiatives.
- Blog: A space to share our insights, progress, and news.
- Contact: Easy access for potential partners and investors to reach out.

Image Suggestions:
- Celestial imagery, cosmic landscapes, and space construction concepts can add a captivating visual element.
- Incorporate a color palette that combines deep space blues with modern metallic tones for a futuristic feel.
- Use high-quality images and graphics that convey the excitement and possibilities of space construction.

Why You Should Join Us:
By taking on this challenge, you'll have the chance to contribute to a groundbreaking mission and be part of the future of space exploration. Your design will be seen by space enthusiasts, investors, and industry experts worldwide.

If you're ready to embark on this cosmic design journey with us, please submit your portfolio and a brief introduction by 22/09/23. We can't wait to see your visionary concepts.

Let's transform the Meridian Vault website into a space of inspiration and innovation. Join us on this incredible adventure!

Best regards,

Tobi
Updates

Target Market(s)

Orbit Service providers, Governments, Space Agencies. Space Infrastructure

Industry/Entity Type

Space, Technology, Innovation, Architecture. Construction

Coding

Coded - Design and coding required

Number of Pages Required

5+ page

Colors
0054AA
0677BA
7BADD7
CADEEF
E8F1F8
6B429C
8869AF
B7A5CE
E3DAEB
F3F0F8

Requirements
Must have
• The logos i have outlined in the website revamp doc, i also need a sub section for FAQs terms of service etc like most professional websites. A page to sell merch. Like our custom hoody, t shirt, key rings, hats, joggers, etc
Nice to have
• any case studies of satellite innovations reaching project completion and how they might relate to my project.

```html
<!DOCTYPE html>
<html lang="en">
<head>
<meta charset="utf-8">
<title>Meridian Vault — Invest in the Future</title>
<link href="https://fonts.googleapis.com/css2?family=Exo+2:wght@600;700;800&family=Kumbh+Sans:wght@400;500;600;700&display=swap" rel="stylesheet">
<style>
:root{
  --blue:#0054AA;
  --blue-mid:#0677BA;
  --blue-light:#7BADD7;
  --navy:#0a1630;
  --navy-deep:#060d20;
  --ink:#111418;
  --text:#555b66;
  --white:#ffffff;
  --line:#d6dbe3;
}
*{box-sizing:border-box;margin:0;padding:0}
html,body{width:1200px;height:4112px;overflow:hidden;background:var(--white)}
body{position:relative;font-family:"Kumbh Sans",sans-serif;color:var(--ink)}
.abs{position:absolute}
.heading{font-family:"Exo 2",sans-serif;font-weight:800;text-transform:uppercase;letter-spacing:.5px}
.btn{position:absolute;display:flex;align-items:center;justify-content:center;border-radius:30px;font-weight:700;font-size:14px;text-transform:uppercase;letter-spacing:.3px}
.btn-solid{background:var(--blue);color:var(--white)}
.btn-white{background:var(--white);color:var(--blue)}
.btn-outline{border:1.5px solid var(--blue);color:var(--blue);background:var(--white);font-size:12px}
.wordmark{font-family:"Kumbh Sans",sans-serif;font-weight:700;color:var(--white);font-size:26px;line-height:1;letter-spacing:1px;text-transform:uppercase}
.arrow-btn{position:absolute;width:42px;height:42px;border-radius:50%;display:flex;align-items:center;justify-content:center}
.arrow-btn.ghost{border:1.5px solid var(--blue);background:var(--white)}
.arrow-btn.fill{background:var(--blue)}
.arrow-btn.ghost-light{border:1.5px solid var(--white)}
.arrow-btn.fill-light{background:var(--white)}

/* hero */
.hero{left:0;top:0;width:1200px;height:647px;background:radial-gradient(ellipse at 78% 45%,#f3a564 0%,#4a5878 9%,#152446 30%,var(--navy-deep) 65%),linear-gradient(#07112a,#0a1a3c)}
.hero-logo{left:112px;top:62px}
.nav{left:511px;top:70px;display:flex;gap:34px;color:var(--white);font-size:15px}
.nav-contact{left:958px;top:61px;width:130px;height:41px;border:1.5px solid var(--white);color:var(--white);border-radius:30px;font-size:15px;font-weight:600;text-transform:none}
.hero-title{left:112px;top:238px;color:var(--white);font-size:46px;line-height:57px}
.hero-text{left:112px;top:371px;width:430px;color:var(--white);font-size:14.5px;line-height:19px}
.hero-btn{left:112px;top:440px;width:153px;height:40px}

/* about */
.about-media{left:112px;top:739px}
.about-title{left:674px;top:738px;font-size:45px;line-height:50px}
.about-text{left:674px;top:862px;width:420px;font-size:14.5px;line-height:22.5px;color:var(--text)}
.about-btn{left:674px;top:1033px;width:153px;height:41px}

/* products */
.products{left:0;top:1154px;width:1200px;height:629px;background:radial-gradient(ellipse at 80% 20%,#1a6fd0 0%,#0d4ea6 40%,#0a3f8c 100%)}
.section-title{font-size:44px;line-height:1}
.product-card{position:absolute;top:1301px;width:359px;height:404px;background:var(--white);border-radius:3px;overflow:hidden}
.product-card .media{height:209px}
.product-card h3{position:absolute;left:30px;top:232px;font-size:18px;font-weight:700}
.product-card p{position:absolute;left:30px;top:265px;width:300px;font-size:10.5px;line-height:18px;color:var(--text)}
.product-card .btn{left:30px;top:338px;width:124px;height:37px}

/* projects */
.project-media{position:absolute;top:1918px;width:356px;height:364px;border-radius:4px}
.project-label{position:absolute;top:2308px;display:flex;align-items:center;gap:16px;font-family:"Kumbh Sans",sans-serif;font-weight:700;font-size:17px;text-transform:uppercase}

/* video */
.video{left:0;top:2455px;width:1200px;height:386px;background:radial-gradient(ellipse at 15% 55%,#e2ecf7 0%,#6f9ed0 12%,#1d3e70 35%,#06101f 70%)}
.play{left:558px;top:2632px;width:88px;height:88px;border-radius:50%;background:var(--white);box-shadow:0 0 0 8px rgba(255,255,255,.35);display:flex;align-items:center;justify-content:center}

/* blog */
.blog-card{position:absolute;top:2980px;width:359px;height:391px;background:var(--white);box-shadow:0 4px 18px rgba(10,22,48,.1);border-radius:3px;overflow:hidden}
.blog-card .media{height:276px}
.blog-card .date{position:absolute;left:26px;top:300px;font-size:11px;font-weight:600}
.blog-card h3{position:absolute;left:26px;top:325px;width:310px;font-size:17.5px;line-height:22px;font-weight:600}

/* cta */
.cta{left:0;top:3511px;width:1200px;height:311px;background:radial-gradient(ellipse at 50% 40%,#0f56b2 0%,#0a3f8f 55%,#08306e 100%)}
.cta-text{left:0;top:3584px;width:1200px;text-align:center;color:var(--white);font-family:"Exo 2",sans-serif;font-weight:700;font-size:36px;line-height:45px}
.cta-btn{left:516px;top:3714px;width:169px;height:42px}

/* footer */
.footer{left:0;top:3822px;width:1200px;height:290px;background:var(--navy)}
.footer-heading{position:absolute;top:3876px;color:var(--white);font-family:"Exo 2",sans-serif;font-weight:700;font-size:17px;line-height:1;text-transform:uppercase}
.footer-links{position:absolute;top:3913px;list-style:none;color:var(--white);font-size:15px;line-height:28.7px}
.social{position:absolute;top:4016px;width:38px;height:38px;border:1.5px solid var(--white);border-radius:50%;display:flex;align-items:center;justify-content:center}
.news-title{left:873px;top:3877px;color:var(--white);font-size:11.5px;font-weight:700;text-transform:uppercase}
.news-form{left:878px;top:3910px;width:194px;height:36px;border:1px solid var(--white);border-radius:20px;display:flex;overflow:hidden}
.news-form span{flex:1;color:#aab3c4;font-size:8.5px;padding-left:18px;display:flex;align-items:center}
.news-form b{width:86px;background:var(--white);color:var(--navy);font-size:11px;display:flex;align-items:center;justify-content:center;border-radius:20px}
.footer-rule{left:112px;top:4077px;width:976px;height:1px;background:rgba(255,255,255,.25)}
.copyright{left:0;top:4088px;width:1200px;text-align:center;color:var(--white);font-size:9.5px}
</style>
</head>
<body>

<!-- Hero -->
<section class="abs hero" role="img" aria-label="Space station orbiting above Earth with sunlight flaring behind it"></section>
<div class="abs hero-logo wordmark">Meridian<br>Vault</div>
<nav class="abs nav"><span>Home</span><span>About Us</span><span>Products &#8964;</span><span>Projects</span><span>Blog</span></nav>
<div class="btn nav-contact">Contact Us</div>
<h1 class="abs heading hero-title">Meridian Vault Invest<br>in the Future</h1>
<p class="abs hero-text">There is a brand-new frontier opening to mankind, and the possibilities are endless.</p>
<div class="btn btn-solid hero-btn">Read More</div>

<!-- About -->
<svg class="abs about-media" width="510" height="322" viewBox="0 0 510 322" role="img" aria-label="Space station above Earth inside a hexagon frame">
  <defs><linearGradient id="aboutFill" x1="0" y1="0" x2="0" y2="1"><stop offset="0" stop-color="#1a1410"/><stop offset=".35" stop-color="#a4643a"/><stop offset=".6" stop-color="#4d78a8"/><stop offset="1" stop-color="#0c1a33"/></linearGradient></defs>
  <polygon points="85,0 425,0 510,161 425,322 85,322 0,161" fill="url(#aboutFill)"/>
  <polyline points="130,0 55,161 130,322" fill="none" stroke="#fff" stroke-width="26"/>
  <polyline points="380,0 455,161 380,322" fill="none" stroke="#fff" stroke-width="26"/>
</svg>
<h2 class="abs heading about-title">About Meridian<br>Vault</h2>
<p class="abs about-text">Meridian Vault is on a mission to reshape the future of space construction. We're pioneers in the field, developing cutting-edge concept construction blocks that promise to redefine how we build beyond our planet's boundaries. Our solutions are scalable, sustainable, and poised to accelerate humanity's journey into the cosmos.</p>
<div class="btn btn-solid about-btn">Read More</div>

<!-- Products -->
<section class="abs products"></section>
<h2 class="abs heading section-title" style="left:48px;top:1222px;color:var(--white)">Our Products</h2>
<div class="btn btn-white" style="left:950px;top:1221px;width:201px;height:41px">View All Products</div>

<article class="product-card" style="left:48px">
  <div class="media" role="img" aria-label="Orbital platform module above Earth" style="background:linear-gradient(160deg,#0c2a66,#2c6fc4 55%,#9cc6ec)"></div>
  <h3>In-Space Platforms</h3>
  <p>Lorem ipsum dolor sit amet, consectetur adipiscing elit, sed do eiusmod tempor incididunt ut labore et dolore magna aliqua.</p>
  <div class="btn btn-outline">Learn More</div>
</article>
<article class="product-card" style="left:421px">
  <div class="media" role="img" aria-label="Capsule with solar panels orbiting Earth" style="background:linear-gradient(160deg,#1a3d6e,#6b94c4 50%,#d9e6f2)"></div>
  <h3>Orbital Power</h3>
  <p>Lorem ipsum dolor sit amet, consectetur adipiscing elit, sed do eiusmod tempor incididunt ut labore et dolore magna aliqua.</p>
  <div class="btn btn-outline">Learn More</div>
</article>
<article class="product-card" style="left:793px">
  <div class="media" role="img" aria-label="Radio dish antenna against a pale sky" style="background:linear-gradient(180deg,#eef1f4,#c9cfd6)"></div>
  <h3>Lumora Networks</h3>
  <p>Lorem ipsum dolor sit amet, consectetur adipiscing elit, sed do eiusmod tempor incididunt ut labore et dolore magna aliqua.</p>
  <div class="btn btn-outline">Learn More</div>
</article>

<div class="arrow-btn ghost-light" style="left:1053px;top:1723px"><svg width="18" height="12" viewBox="0 0 18 12"><path d="M17 6H2M7 1 2 6l5 5" fill="none" stroke="#fff" stroke-width="1.6"/></svg></div>
<div class="arrow-btn fill-light" style="left:1109px;top:1723px"><svg width="18" height="12" viewBox="0 0 18 12"><path d="M1 6h15M11 1l5 5-5 5" fill="none" stroke="#0054AA" stroke-width="1.6"/></svg></div>

<!-- Projects -->
<h2 class="abs heading section-title" style="left:48px;top:1839px">Current Projects</h2>
<div class="btn btn-solid" style="left:950px;top:1840px;width:201px;height:42px">View All Projects</div>

<div class="project-media" style="left:49px;background:radial-gradient(circle at 50% 55%,#7fa6cf 0%,#3d5a7e 30%,#15202e 70%)" role="img" aria-label="Earth seen through a space station observation window"></div>
<div class="project-media" style="left:421px;background:linear-gradient(180deg,#05081a 0%,#1b2c55 45%,#3d78a8 75%,#6d9a6a 100%)" role="img" aria-label="Satellite beaming a network grid onto Earth"></div>
<div class="project-media" style="left:793px;background:linear-gradient(180deg,#2a3a78 0%,#5b6ea8 55%,#e8ecf4 100%)" role="img" aria-label="Rocket climbing above the clouds"></div>

<div class="project-label" style="left:50px">Telescopes on the Moon <svg width="36" height="14" viewBox="0 0 36 14"><path d="M0 7h34M28 1l6 6-6 6" fill="none" stroke="#0054AA" stroke-width="2"/></svg></div>
<div class="project-label" style="left:421px">Corvid Test Rig <svg width="36" height="14" viewBox="0 0 36 14"><path d="M0 7h34M28 1l6 6-6 6" fill="none" stroke="#0054AA" stroke-width="2"/></svg></div>
<div class="project-label" style="left:793px">Biomass Adaptors <svg width="36" height="14" viewBox="0 0 36 14"><path d="M0 7h34M28 1l6 6-6 6" fill="none" stroke="#0054AA" stroke-width="2"/></svg></div>

<div class="arrow-btn ghost" style="left:49px;top:2367px"><svg width="18" height="12" viewBox="0 0 18 12"><path d="M17 6H2M7 1 2 6l5 5" fill="none" stroke="#0054AA" stroke-width="1.6"/></svg></div>
<div class="arrow-btn fill" style="left:105px;top:2367px"><svg width="18" height="12" viewBox="0 0 18 12"><path d="M1 6h15M11 1l5 5-5 5" fill="none" stroke="#fff" stroke-width="1.6"/></svg></div>

<!-- Video -->
<section class="abs video" role="img" aria-label="Satellite orbiting Earth at sunrise, video preview"></section>
<div class="abs play"><svg width="28" height="30" viewBox="0 0 28 30"><path d="M3 1l24 14L3 29z" fill="#0054AA"/></svg></div>

<!-- Blog -->
<h2 class="abs heading section-title" style="left:48px;top:2901px">Latest Blog</h2>
<div class="btn btn-solid" style="left:980px;top:2900px;width:169px;height:41px">View All Blog</div>

<article class="blog-card" style="left:49px">
  <div class="media" role="img" aria-label="Scientist in a laboratory" style="background:linear-gradient(120deg,#c9d6dc,#7f9aa6 60%,#3c5662)"></div>
  <div class="date">28 JUL, 2023</div>
  <h3>Kestrel Robotics Contributes To Sable-R</h3>
</article>
<article class="blog-card" style="left:421px">
  <div class="media" role="img" aria-label="Space shuttle launching in front of the Moon" style="background:radial-gradient(ellipse at 50% 35%,#6a6e78 0%,#2b2e38 45%,#0c0d12 80%)"></div>
  <div class="date">MARCH 28, 2023</div>
  <h3>Join The Space Catalogue</h3>
</article>
<article class="blog-card" style="left:790px">
  <div class="media" role="img" aria-label="Satellite above a glowing blue Earth" style="background:linear-gradient(170deg,#0a2f6e,#1f6bc4 55%,#0b3a7c)"></div>
  <div class="date">28 JUL, 2023</div>
  <h3>'Call For Interest Of Secondary Payload On Halcyon +</h3>
</article>

<div class="arrow-btn ghost" style="left:1053px;top:3414px"><svg width="18" height="12" viewBox="0 0 18 12"><path d="M17 6H2M7 1 2 6l5 5" fill="none" stroke="#0054AA" stroke-width="1.6"/></svg></div>
<div class="arrow-btn fill" style="left:1109px;top:3414px"><svg width="18" height="12" viewBox="0 0 18 12"><path d="M1 6h15M11 1l5 5-5 5" fill="none" stroke="#fff" stroke-width="1.6"/></svg></div>

<!-- Call to action -->
<section class="abs cta"></section>
<p class="abs cta-text">Join us on the journey to the stars. Explore the<br>limitless possibilities of space infrastructure today!</p>
<div class="btn btn-white cta-btn">Contact Us</div>

<!-- Footer -->
<footer class="abs footer"></footer>
<div class="abs wordmark" style="left:112px;top:3890px">Meridian<br>Vault</div>
<div class="social" style="left:113px"><svg width="12" height="12"><circle cx="6" cy="6" r="4" fill="#fff"/></svg></div>
<div class="social" style="left:168px"><svg width="12" height="12"><circle cx="6" cy="6" r="4" fill="#fff"/></svg></div>
<div class="social" style="left:221px"><svg width="12" height="12"><circle cx="6" cy="6" r="4" fill="#fff"/></svg></div>

<h4 class="footer-heading" style="left:324px">Explore</h4>
<ul class="footer-links" style="left:324px"><li>About Us</li><li>Products</li><li>Projects</li><li>Blog</li><li>Contact</li></ul>
<h4 class="footer-heading" style="left:487px">Capabilities</h4>
<ul class="footer-links" style="left:487px"><li>Transportation</li><li>Destinations</li><li>Applications</li></ul>
<h4 class="footer-heading" style="left:686px">Capabilities</h4>
<ul class="footer-links" style="left:686px"><li>Transportation</li><li>Destinations</li><li>Applications</li></ul>

<div class="abs news-title">Subscribe to our newsletter</div>
<div class="abs news-form"><span>Enter your email</span><b>Subscribe</b></div>

<div class="abs footer-rule"></div>
<div class="abs copyright">© Copyright 2023 Meridian Vault 2023.All rights reserved</div>

</body>
</html>
```